Surgical Conditions of the thyroid and parathyroid glands - a flyer for GPs

Hi there,

I am a thyroid surgeon trying to produce a bi-fold A4 flyer as a quick reference guide for general practitioners (family doctors). It needs to feel friendly and professional.

The text for the four "pages" can be found in the "thyroid flyer for design" document attached.

The front page should have:
- The title
- the photo with the patient having an ultrasound
- the photo of the asian woman with the enlarged thyroid gland
- possibly the photo of the blonde woman touching her neck

The inner two pages are predominantly text - I would love this to be presented in an easy to read, uncluttered format. There is a photo attached which demonstrates the parathyroid glands. This should be placed near the parathyroid text section if possible.

The back page is a brief bio of myself. It should have the profile pic attached.
It should have contact details, which I forgot to put in the word document. These details are:
Phone (03) 9482 5170 for all appointments
Consulting at:
18 Wattlebird Lane, Berwick, VIC 3806
hollowaymedicalteam.com.au
dorianpelsworth.com

The back page should also have the "Tarrow Care" and "Guild of Operators" logos.

If possible, all pages should have the "Holloway Medical Team" logo.

The whole feel could have a similar colour scheme to my group website (largely orange and green). Please see www.hollowaymedicalteam.com.au for examples.

Many thanks!

Target Market(s)

General practitioners (ie family doctors)

Industry/Entity Type

Medical And Science

Font styles to use
Sans Serif

Colors
33b8a4
f78f20

Requirements
Must have
• Contact details on the back, holloway medical team logo on front and back pages, Tarrow Care and Guild of Operators logo on the back.
Nice to have
• Other medical/surgical related images as you see fit - sorry to be so broad!!

```html
<!DOCTYPE html>
<html lang="en">
<head>
<meta charset="utf-8">
<title>Surgical Conditions of the Thyroid and Parathyroid Glands – GP Guide</title>
<link href="https://fonts.googleapis.com/css2?family=Source+Sans+3:wght@300;400;600;700&display=swap" rel="stylesheet">
<style>
:root{
  --teal:#33b8a4;
  --orange:#f78f20;
  --pink:#e4398a;
  --blue:#1f9ad6;
  --ink:#4f5355;
  --paper:#ffffff;
  --bg:#e6e8e9;
}
*{box-sizing:border-box;margin:0;padding:0}
html,body{width:1200px;height:1200px;overflow:hidden;background:var(--bg);font-family:"Source Sans 3",sans-serif;color:var(--ink)}
.sheet{position:absolute;display:flex;box-shadow:0 6px 20px rgba(0,0,0,.15)}
.sheet--inside{left:204px;top:24px}
.sheet--outside{left:204px;top:608px}
.page{position:relative;width:396px;height:564px;background:var(--paper);overflow:hidden;font-size:7.2px;line-height:1.3}
.page + .page{border-left:1px solid #e2e4e5}
h2{font-weight:600;font-size:11px;margin-bottom:5px}
h3{font-weight:700;font-size:8px;margin-bottom:3px}
b{font-weight:700;color:#333}
p{margin-bottom:5px}
ul{list-style:none}
li{padding-left:8px;position:relative;margin-bottom:3px}
li::before{content:"";position:absolute;left:0;top:3px;width:3px;height:3px;border-radius:50%;background:var(--blue)}
.brand{display:flex;align-items:center;gap:6px;font-weight:700;color:#3b3f41;white-space:nowrap}
.brand__dot{width:16px;height:16px;border-radius:50%;background:var(--teal);flex:none}
/* inner left */
.anatomy{height:190px;background:radial-gradient(ellipse at 55% 45%,#dfe7e6 0%,#b8d7d1 35%,var(--teal) 80%)}
.disorders{display:grid;grid-template-columns:1fr 1fr;gap:14px;padding:16px 22px 10px}
.disorders h2{color:var(--teal)}
.disorders p{margin-bottom:4px}
.symptoms{position:absolute;left:0;right:0;bottom:0;height:170px;padding:16px 22px;background:linear-gradient(180deg,var(--orange) 0%,#f9b35d 55%,#fde7c8 100%);color:#fff}
.symptoms h2{color:#fff;font-weight:300;font-size:12px}
.symptoms__cols{display:grid;grid-template-columns:repeat(3,1fr);gap:10px}
.symptoms h3{color:#4a3a20}
.symptoms span{display:block;font-size:7.8px;line-height:1.35}
/* inner right */
.workup{padding:26px 24px 0}
.workup h2{color:var(--pink)}
.workup__cols{display:grid;grid-template-columns:1fr 1fr;gap:16px;padding:10px 24px}
.h-blue{color:var(--blue)}
.h-orange{color:var(--orange)}
.page--workup .brand{position:absolute;right:24px;bottom:26px;font-size:12px}
/* back */
.bio-top{display:flex;padding:20px 20px 0}
.portrait{width:118px;height:96px;flex:none;background:linear-gradient(135deg,#cfd6d9,#8d9498)}
.bio-head{padding-left:14px}
.bio-head h2{color:var(--teal)}
.bio-cols{display:grid;grid-template-columns:118px 1fr 1fr;gap:12px;padding:8px 20px}
.badges{display:flex;flex-direction:column;gap:8px;padding-top:4px}
.badge{width:60px;height:18px;background:#c9d0d6}
.badge--round{width:18px;border-radius:50%;background:#c83a3a}
.lists{display:grid;grid-template-columns:118px 1fr 1fr;gap:12px;padding:0 20px}
.lists span{display:block}
.back-foot{position:absolute;left:20px;right:20px;bottom:22px;display:grid;grid-template-columns:118px 1fr 1fr;gap:12px;align-items:end}
.back-foot .brand{font-size:9px;gap:5px}
.back-foot .brand__dot{width:12px;height:12px}
.site{color:var(--teal);font-weight:600;font-size:8.5px}
.site--dark{color:#4f5355}
/* front */
.page--cover{background:linear-gradient(160deg,#7fd3c4 0%,var(--teal) 40%,#5cc6b4 60%)}
.cover-photo{position:absolute}
.cover-photo--neck{right:0;top:0;width:250px;height:250px;background:radial-gradient(ellipse at 60% 40%,#f3d4c3 0%,#e8bca6 45%,rgba(51,184,164,0) 72%)}
.cover-photo--goitre{left:0;bottom:60px;width:220px;height:240px;background:radial-gradient(ellipse at 35% 55%,#f0c8a4 0%,#e7b081 40%,rgba(247,143,32,.3) 66%,rgba(51,184,164,0) 80%)}
.cover-photo--scan{right:8px;top:250px;width:200px;height:160px;background:radial-gradient(ellipse at 60% 55%,#f4b96a 0%,rgba(247,185,106,.6) 45%,rgba(247,143,32,0) 75%)}
.cover-glow{position:absolute;left:0;right:0;top:210px;height:180px;background:linear-gradient(180deg,rgba(247,143,32,0),rgba(247,143,32,.45) 50%,rgba(255,255,255,0))}
.cover-title{position:absolute;left:28px;right:24px;top:208px;color:#fff}
.cover-title h1{font-weight:300;font-size:22px;line-height:1.05;letter-spacing:.5px;text-transform:uppercase}
.cover-title p{font-weight:300;font-size:15px;margin-top:6px}
.cover-base{position:absolute;left:0;right:0;bottom:0;height:130px;background:linear-gradient(180deg,rgba(255,255,255,0),#fff 55%)}
.page--cover .brand{position:absolute;right:26px;bottom:26px;font-size:16px;flex-direction:column;align-items:center;gap:5px}
.page--cover .brand__dot{width:34px;height:34px}
.cover-edge{position:absolute;right:0;top:0;bottom:0;width:8px;background:var(--teal)}
</style>
</head>
<body>

<section class="sheet sheet--inside">
  <article class="page page--disorders">
    <div class="anatomy" role="img" aria-label="Illustration of the neck showing the thyroid and the four parathyroid glands"></div>
    <div class="disorders">
      <div>
        <h2>Common thyroid disorders</h2>
        <p><b>Solitary nodules</b> – often require characterisation with ultrasound +/- fine needle aspirate to determine likelihood of malignancy</p>
        <p><b>Graves' disease</b> – autoimmune stimulation of TSH receptors leading to hyperthyroidism</p>
        <p><b>Thyroid cancer</b> – important risk factors include family history and a history of radiation exposure. Readily treatable with surgery, often in conjunction with radioactive iodine</p>
      </div>
      <div>
        <p><b>Hashimoto's thyroiditis</b> – usually self-limiting, can cause hyperthyroidism (early) or hypothyroidism (late). May benefit from surgery if associated with ongoing pain</p>
        <p><b>Thyroglossal cyst</b> – presents as a midline lump above the thyroid cartilage (Adam's apple), may become inflamed or form fistulas to the overlying skin</p>
        <p><b>Multinodular goitre</b> – usually benign but may cause compressive symptoms</p>
      </div>
    </div>
    <div class="symptoms">
      <h2>Common symptoms of thyroid disease</h2>
      <div class="symptoms__cols">
        <div><h3>Symptoms of hyperthyroidism</h3><span>Tiredness</span><span>Palpitations</span><span>Tremor</span><span>Sweats</span><span>Heat intolerance</span><span>Exophthalmos</span><span>Diarrhoea</span><span>Weight loss</span></div>
        <div><h3>Symptoms of hypothyroidism</h3><span>Lethargy</span><span>Weight gain</span><span>Weakness</span><span>Cold</span><span>Hair loss</span></div>
        <div><h3>Compressive symptoms</h3><span>Lump in the neck</span><span>Dysphagia</span><span>Dyspnoea</span><span>Voice change</span></div>
      </div>
    </div>
  </article>

  <article class="page page--workup">
    <div class="workup">
      <h2>Workup for thyroid disorders</h2>
      <p>Most thyroid disorders requiring surgical intervention can be diagnosed with a <b>thyroid ultrasound</b> and <b>thyroid function tests</b>.</p>
      <p>If a patient is biochemically hyperthyroid, a <b>thyroid nuclear scan</b> and <b>anti-TSH receptor antibodies</b> are useful to determine the underlying cause (eg Graves' disease, toxic nodule or toxic goitre). <b>Thyroid antibodies</b> can also determine if there is underlying thyroiditis. All patients with thyroid disease should also undergo screening for concurrent parathyroid disease with <b>PTH</b>, <b>calcium</b> and <b>vitamin D</b> levels.</p>
      <p>A nodule with suspicious features on ultrasound (increased vascularity, microcalcifications, irregular border) should undergo <b>ultrasound-guided fine needle aspirate</b>.</p>
    </div>
    <div class="workup__cols">
      <div>
        <h2 class="h-blue">Which nodules should undergo fine needle aspirate?</h2>
        <ul>
          <li>Nodules &lt;1 cm</li>
          <li>If there are suspicious features on ultrasound (irregular border, microcalcifications, increased vascularity)</li>
          <li>Nodules without suspicious features less than 1 cm can be re-evaluated with an ultrasound in 1 year</li>
          <li>Nodules 1 to 3 cm</li>
          <li>Should undergo FNA, especially if there are suspicious features</li>
          <li>Nodules &gt;3cm</li>
          <li>Should undergo FNA</li>
          <li>These nodules are more likely to become symptomatic and there is an increased risk of a false negative FNA</li>
        </ul>
      </div>
      <div>
        <p>with nodules of this size. They should therefore be considered for excision via a hemithyroidectomy. An FNA can determine if a total thyroidectomy is preferred in the case of malignancy.</p>
        <h2 class="h-orange">Parathyroid disease</h2>
        <p>Simple screening with <b>calcium</b> and <b>PTH</b> levels can detect hyperparathyroidism before symptoms become evident. Patients with osteoporosis, recurrent kidney stones or pathological fractures should be tested, as well as with an <b>ultrasound</b> to look for concurrent thyroid issues.</p>
      </div>
    </div>
    <div class="brand"><span class="brand__dot"></span>Holloway Medical Team</div>
  </article>
</section>

<section class="sheet sheet--outside">
  <article class="page page--back">
    <div class="bio-top">
      <div class="portrait" role="img" aria-label="Portrait of the surgeon seated at his desk"></div>
      <div class="bio-head">
        <h2>About Dorian</h2>
        <p>Dorian is a graduate of Kellbrook University (Bachelor of Medicine, Bachelor of Surgery, 2000) and has been a fellow of the Royal Australasian Guild of Operators since 2009.</p>
      </div>
    </div>
    <div class="bio-cols">
      <div class="badges"><span class="badge badge--round"></span><span class="badge"></span><span class="badge"></span></div>
      <div>
        <p>Dorian's surgical interests include benign and malignant disease of the thyroid and parathyroid glands, endoscopic trans-axillary and trans-oral thyroid surgery, and management of adrenal disease. He is the head of paediatric endocrine surgery at Tarrow Children's Hospital.</p>
        <p>He is happy to perform ultrasound-guided fine needle aspirates for most thyroid nodules as required, at an advantage to patients in terms of time and cost.</p>
      </div>
      <div>
        <p>Away from medicine, Dorian is a classically-trained flautist and jazz saxophonist who plays with the Southern Physicians Ensemble. He is a keen follower of the Riverbend football club and the Sri Lankan cricket team. Dorian travels to Sri Lanka regularly with projectHEAL, a charity currently building a trauma centre on the east coast, a region affected by the Boxing Day tsunami and civil war.</p>
        <p>Dorian has public appointments with Tarrow Care (Ashcombe, Dunmore, Fernvale and Marlowe), Eastern Care Network and St Aldric's. He is an accredited specialist surgeon at The Glen, The Crescent, Linwood Richmond and St Brennan Private Hospitals.</p>
      </div>
    </div>
    <div class="lists">
      <div></div>
      <div><h3>Endocrine conditions:</h3><span>Thyroid nodules</span><span>Thyroid cancer</span><span>Graves' disease/thyrotoxicosis</span><span>Multinodular goitre</span><span>Parathyroid disease</span><span>Adrenal disease</span></div>
      <div><h3>General surgical conditions:</h3><span>Laparoscopic cholecystectomy</span><span>Abdominal hernias (inguinal, umbilical, incisional)</span><span>Lipomas</span><span>Skin lesions</span><span>Carpal tunnel release</span><span>Ingrown toenails</span><span>Vasectomy</span></div>
    </div>
    <div class="back-foot">
      <div class="brand"><span class="brand__dot"></span>Holloway Medical Team</div>
      <div><h3>For all appointments</h3><p>Phone (03) 9482 5170</p><p class="site">hollowaymedicalteam.com.au</p></div>
      <div><h3>Consulting at:</h3><p>18 Wattlebird Lane, Fernvale, VIC 3999</p><p class="site site--dark">dorianpelsworth.com</p></div>
    </div>
  </article>

  <article class="page page--cover">
    <div class="cover-photo cover-photo--neck" role="img" aria-label="Photo of a woman touching her neck"></div>
    <div class="cover-glow"></div>
    <div class="cover-photo cover-photo--scan" role="img" aria-label="Photo of a surgeon performing a neck ultrasound on a patient"></div>
    <div class="cover-photo cover-photo--goitre" role="img" aria-label="Photo of a woman with an enlarged thyroid gland"></div>
    <div class="cover-title">
      <h1>Surgical conditions of the thyroid and parathyroid glands</h1>
      <p>A quick reference guide for GPs</p>
    </div>
    <div class="cover-base"></div>
    <div class="brand"><span class="brand__dot"></span>Holloway Medical Team</div>
    <div class="cover-edge"></div>
  </article>
</section>

</body>
</html>
```